This Project is listed for : Vexmoor only ... if you are not Vexmoors, please do not submit please

This is the listing for

Torbesca

business cards
very simple, elegant and firm
Black / Red / White

Target Market(s)

Adults
Investors
Clients

Industry/Entity Type

Business

Font styles to use
Decorative
Script

```html
<!DOCTYPE html>
<html lang="en">
<head>
<meta charset="utf-8">
<title>Torbesca Business Cards</title>
<link href="https://fonts.googleapis.com/css2?family=Pinyon+Script&family=Open+Sans:wght@400&display=swap" rel="stylesheet">
<style>
  :root {
    --page-bg: #ececea;
    --card-white: #ffffff;
    --card-red: #de1b22;
    --accent-red: #e0343a;
    --ink-black: #141414;
    --ink-grey: #3a3a3a;
    --rule: #2a2a2a;
  }
  * { margin: 0; padding: 0; box-sizing: border-box; }
  html, body { width: 1200px; height: 1023px; overflow: hidden; }
  body {
    background: var(--page-bg);
    font-family: "Open Sans", Arial, sans-serif;
    position: relative;
  }
  .card {
    position: absolute;
    left: 230px;
    width: 740px;
    height: 423px;
    border-radius: 28px;
    box-shadow: 0 6px 18px rgba(0,0,0,0.18);
    overflow: hidden;
  }
  .card-front { top: 60px; background: var(--card-white); }
  .card-back  { top: 540px; background: var(--card-red); }

  .script { font-family: "Pinyon Script", "Brush Script MT", cursive; font-weight: 400; }

  .front-business {
    position: absolute; left: 60px; top: 48px;
    font-size: 54px; color: var(--accent-red); line-height: 1;
  }
  .front-person { position: absolute; left: 60px; top: 168px; }
  .person-name { font-size: 44px; color: var(--accent-red); line-height: 1; }
  .person-role { font-size: 22px; color: var(--ink-grey); margin-top: 2px; }

  .front-rule {
    position: absolute; left: 60px; right: 60px; top: 292px;
    height: 2px; background: var(--rule);
  }
  .front-contact {
    position: absolute; right: 70px; top: 312px;
    list-style: none; font-size: 22px; color: var(--ink-black); line-height: 1.3;
  }
  .front-contact li { display: flex; align-items: center; gap: 10px; }
  .front-contact svg { width: 18px; height: 18px; flex: none; }

  .back-business {
    position: absolute; inset: 0;
    display: flex; align-items: center; justify-content: center;
    font-size: 76px; color: var(--ink-black);
  }
</style>
</head>
<body>
  <section class="card card-front">
    <h1 class="front-business script">Business Name Here</h1>
    <div class="front-person">
      <p class="person-name script">Your name</p>
      <p class="person-role">Designation</p>
    </div>
    <div class="front-rule"></div>
    <ul class="front-contact">
      <li>
        <svg viewBox="0 0 18 18" aria-hidden="true">
          <rect width="18" height="18" rx="2" fill="var(--accent-red)"/>
          <path d="M4 6c0-1 1-2 5-2s5 1 5 2v1h-3V6H7v1H4z M5 8h8l1 6H4z" fill="#fff"/>
        </svg>
        <span>555 014 287</span>
      </li>
      <li>
        <svg viewBox="0 0 18 18" aria-hidden="true">
          <rect width="18" height="18" rx="2" fill="var(--accent-red)"/>
          <path d="M3 5h12v8H3z" fill="none" stroke="#fff" stroke-width="1.4"/>
          <path d="M3 5l6 5 6-5" fill="none" stroke="#fff" stroke-width="1.4"/>
        </svg>
        <span>mail@vexo.test</span>
      </li>
    </ul>
  </section>

  <section class="card card-back">
    <h2 class="back-business script">Business Name Here</h2>
  </section>
</body>
</html>
```